Card for invoking rights with police

Our criminal defense law firm is seeking proposals for a design for our card intended for clients to carry with them in their car. Upon being pulled over, they would hand this card to the officer.
Text for the back of the card:
"For Law Enforcement:"
"I will comply with lawful orders but respectfully decline any test or other requests without my attorney. I wish to remain silent, do not consent to searches, and request to speak with my attorney now.
The back of the card should prominently feature the text and the firm logo should be secondary.
Front
Must prominently feature contact info: 503-555-0182. Do not include attorney name, email, phone from the example file. This is intended to be generic for the firm and not tied to an individual lawyer.
Included for design reference: current business card, firm logo.
We intend to use trenvo.com to produce the cards.
Updates
The back of the card should prominently display the text regarding invocation of rights. Please title it "For Law Enforcement".
Target Market(s)
People who have been stopped by police
Contact Information for Business Card
see project description
Look and feel

```html
<!DOCTYPE html>
<html lang="en">
<head>
<meta charset="utf-8">
<title>Halvorsen Law Firm – Rights Card</title>
<link href="https://fonts.googleapis.com/css2?family=Open+Sans:wght@400;600;700&display=swap" rel="stylesheet">
<style>
  :root {
    --navy: #0c2748;
    --paper: #ffffff;
    --ink: #3a3d42;
    --backdrop: #ecebe8;
  }
  * { box-sizing: border-box; margin: 0; padding: 0; }
  html, body { width: 1200px; height: 960px; overflow: hidden; }
  body {
    background: var(--backdrop);
    font-family: "Open Sans", Arial, sans-serif;
    position: relative;
  }
  .card {
    position: absolute;
    width: 600px;
    height: 343px;
    overflow: hidden;
    box-shadow: 0 6px 18px rgba(0,0,0,0.12);
  }
  .brand {
    position: absolute;
    display: flex;
    align-items: center;
    gap: 12px;
  }
  .brand__mark { flex: none; }
  .brand__name {
    font-weight: 400;
    white-space: nowrap;
  }

  /* Back face */
  .card--back {
    left: 40px; top: 110px;
    background: var(--navy);
    color: var(--paper);
  }
  .card--back .brand { left: 50%; transform: translateX(-50%); top: 38px; }
  .card--back .brand__mark { width: 30px; height: 30px; background: var(--paper); }
  .card--back .brand__name { color: var(--paper); font-size: 16px; letter-spacing: 0.2em; }
  .rights {
    position: absolute;
    left: 56px; right: 56px; top: 112px;
    text-align: center;
  }
  .rights__title {
    font-weight: 700;
    font-size: 22px;
    letter-spacing: 0.08em;
    text-transform: uppercase;
    margin-bottom: 16px;
  }
  .rights__statement {
    font-size: 15px;
    line-height: 1.6;
  }

  /* Front face */
  .card--front {
    left: 560px; top: 510px;
    background: var(--paper);
    color: var(--ink);
  }
  .card--front .brand { left: 322px; top: 60px; gap: 10px; }
  .card--front .brand__mark { width: 36px; height: 36px; background: var(--navy); }
  .card--front .brand__name { color: var(--navy); font-size: 15px; letter-spacing: 0.14em; }
  .phone-band {
    position: absolute;
    left: 0; top: 92px;
    width: 306px; height: 62px;
    background: var(--navy);
    color: var(--paper);
    display: flex;
    align-items: center;
    gap: 12px;
    padding-left: 34px;
  }
  .phone-band svg { width: 20px; height: 20px; fill: var(--paper); flex: none; }
  .phone-band__number { font-weight: 700; font-size: 26px; letter-spacing: 0.02em; }
  .address {
    position: absolute;
    right: 40px; top: 150px;
    text-align: right;
    font-style: normal;
    font-size: 13.5px;
    line-height: 1.45;
    color: var(--ink);
  }
  .website {
    position: absolute;
    left: 34px; top: 290px;
    display: flex;
    align-items: center;
    gap: 8px;
    font-size: 15px;
    color: var(--ink);
  }
  .website svg { width: 12px; height: 12px; fill: var(--navy); flex: none; }
</style>
</head>
<body>

<section class="card card--back" aria-label="Card back">
  <div class="brand">
    <span class="brand__mark"></span>
    <span class="brand__name">HALVORSEN LAW FIRM</span>
  </div>
  <div class="rights">
    <h1 class="rights__title">For Law Enforcement:</h1>
    <p class="rights__statement">I will comply with lawful orders but respectfully decline any test or other requests without my attorney. I wish to remain silent, do not consent to searches, and request to speak with my attorney now.</p>
  </div>
</section>

<section class="card card--front" aria-label="Card front">
  <div class="brand">
    <span class="brand__mark"></span>
    <span class="brand__name">HALVORSEN LAW FIRM</span>
  </div>
  <div class="phone-band">
    <svg viewBox="0 0 12 12" aria-hidden="true"><path d="M1 3.5C1 2 2.5 1 6 1s5 1 5 2.5L9 5 8 3.5H4L3 5zM3 6h6l1 5H2z"/></svg>
    <span class="phone-band__number">503-555-0182</span>
  </div>
  <address class="address">
    2150 Harbor View Ave<br>
    Suite 210<br>
    Bellmont, WA 98110
  </address>
  <p class="website"><svg viewBox="0 0 12 12" aria-hidden="true"><circle cx="6" cy="6" r="6"/><path d="M1 6h10M6 1v10" stroke="#fff" stroke-width="1"/></svg>www.halvorsenlaw.com</p>
</section>

</body>
</html>
```